Thistlewood Candles, Hand-poured scented soy candles

Create a logo and label design to use on my vintage country farmhouse style, all natural, hand poured soy candle jars and apothecaries. Candles will be labeled in 4 different sizes so design must be adaptable, clean, simple, telegraphic and invoke interest in the product. Think Black lettering on white or black on kraft brown. Thistlewood is the area code for New Hampshire where we make them. The labels will need a prominent area for the scent of the candle to be listed that the eyes are drawn to. Primitive country in design? Use of state attractions? Jars are a square mason style 8 ounce and 16 ounce. Tarts are a clamshell. Lids are a 70-400 series 2.5" label area. Candles are white in a clear glass jar, black lids. There will be label design sizes of 3"x 2.5" 2.5" round, 1.5"x2.5"

Target Market(s)

primitive country, farmhouse, vintage, general home decor

Contact Information for Business Card

Thistlewood Candles, all natural soy candles, hand-poured in New Hampshire, logo, phone, address. Possibly match the main label.

Logo Text

Thistlewood Candles, all natural soy candles, hand-poured in New Hampshire, area for scent description and size of container.

Font styles to use
Serif
Script

Colors

Designer to choose colors to be used in the design.

Requirements
Must have
• simple and clean, country farmhouse with a bit of vintage thrown in. possibly multiple fonts to distinguish info from scent name
Nice to have
• at this time I am open to suggestions
• Prefer scent names or brand name in an older script?
• older copperplate/Spencerian?
Should not have
• cluttered, busy, too modern, multiple colors

```html
<!DOCTYPE html>
<html lang="en">
<head>
<meta charset="utf-8">
<title>Thistlewood Candles — Jar Label</title>
<link href="https://fonts.googleapis.com/css2?family=Marcellus&family=Cormorant+Garamond:wght@500;600&display=swap" rel="stylesheet">
<style>
  :root {
    --page: #ffffff;
    --paper: #ececec;
    --paper-light: #f3f3f3;
    --ink: #2b2b2b;
    --ink-soft: #555555;
    --illustration: #4a4a4a;
    --illustration-faded: #dedede;
    --dots: #9a9a9a;
  }
  html, body {
    margin: 0;
    padding: 0;
    width: 1200px;
    height: 1000px;
    overflow: hidden;
    background: var(--page);
  }
  .canvas {
    position: relative;
    width: 1200px;
    height: 1000px;
  }
  .label {
    position: absolute;
    left: 38px;
    top: 173px;
    width: 1124px;
    height: 655px;
    overflow: hidden;
    background:
      radial-gradient(circle at 20% 30%, var(--paper-light) 0, transparent 40%),
      radial-gradient(circle at 75% 70%, var(--paper-light) 0, transparent 45%),
      var(--paper);
    box-shadow: 0 2px 6px rgba(0,0,0,0.35);
    color: var(--ink);
    font-family: "Marcellus", serif;
  }
  .backdrop-illustration {
    position: absolute;
    left: 537px;
    top: 247px;
    width: 587px;
    height: 408px;
    background: linear-gradient(180deg, rgba(222,222,222,0.5) 0%, var(--illustration-faded) 60%, rgba(222,222,222,0.7) 100%);
  }
  .farmhouse-illustration {
    position: absolute;
    left: 360px;
    top: 52px;
    width: 394px;
    height: 203px;
    background: linear-gradient(180deg, #6a6a6a 0%, var(--illustration) 100%);
  }
  .fine-print {
    position: absolute;
    left: 52px;
    top: 70px;
    height: 448px;
    margin: 0;
    writing-mode: vertical-rl;
    transform: rotate(180deg);
    font-family: "Cormorant Garamond", serif;
    font-weight: 500;
    font-size: 10.4px;
    line-height: 13px;
    letter-spacing: 0.3px;
    text-transform: uppercase;
    color: var(--ink-soft);
    text-align: left;
  }
  .net-weight {
    position: absolute;
    left: 44px;
    top: 530px;
    height: 82px;
    margin: 0;
    writing-mode: vertical-rl;
    transform: rotate(180deg);
    font-family: "Cormorant Garamond", serif;
    font-weight: 600;
    font-size: 34px;
    line-height: 42px;
    letter-spacing: 3px;
    text-align: center;
  }
  .brand {
    position: absolute;
    left: 360px;
    top: 272px;
    width: 394px;
  }
  .brand-row {
    display: flex;
    align-items: center;
    justify-content: space-between;
  }
  .established {
    display: flex;
    flex-direction: column;
    align-items: center;
    gap: 6px;
    font-size: 15px;
    letter-spacing: 1.5px;
    margin-top: -44px;
  }
  .established::before,
  .established::after {
    content: "";
    display: block;
    width: 48px;
    height: 3px;
    background: var(--ink);
  }
  .brand-name {
    font-size: 38px;
    line-height: 54px;
    letter-spacing: 1.5px;
    text-align: center;
    color: var(--ink);
    margin: 0;
    font-weight: 400;
  }
  .tagline {
    position: absolute;
    left: 290px;
    top: 486px;
    width: 497px;
    text-align: center;
    font-family: "Marcellus", serif;
    color: var(--ink);
    letter-spacing: 2.8px;
  }
  .tagline-primary {
    font-size: 25px;
    margin: 0 0 12px;
  }
  .divider {
    height: 0;
    border-top: 2px dotted var(--dots);
    margin: 0 0 14px;
  }
  .tagline-origin {
    font-size: 25px;
    line-height: 29px;
    margin: 0;
  }
</style>
</head>
<body>
<div class="canvas">
  <section class="label">
    <div class="backdrop-illustration" role="img" aria-label="Faded large drawing of the farmhouse with pine trees"></div>
    <div class="farmhouse-illustration" role="img" aria-label="Drawing of a two-storey farmhouse with porch, flanked by pine trees"></div>

    <p class="fine-print">
      Lorem ipsum dolor sit amet, consectetuer adipiscing elit, sed diam<br>
      nonummy nibh euismod tincidunt ut laoreet dolore magna aliquam erat<br>
      volutpat. Ut wisi enim ad minim veniam, quis nostrud exerci tation<br>
      ullamcorper suscipit lobortis nisl ut aliquip ex ea commodo<br>
      consequat. Duis autem vel eum iriure dolor in hendrerit in vulputate<br>
      velit esse molestie consequat, vel illum dolore eu
    </p>
    <p class="net-weight">300<br>GM</p>

    <div class="brand">
      <div class="brand-row">
        <span class="established">EST.</span>
        <h1 class="brand-name">THISTLEWOOD<br>CANDLES</h1>
        <span class="established">2019</span>
      </div>
    </div>

    <div class="tagline">
      <p class="tagline-primary">ALL NATURAL SOY CANDLES</p>
      <div class="divider"></div>
      <p class="tagline-origin">HAND-POURED IN<br>NEW HAMPSHIRE</p>
    </div>
  </section>
</div>
</body>
</html>
```